Business Card Design - Local Discount Club

Looking for a fun business card for a local discount club. One side should be the logo only and the other should be have :

Name
Title
Phone, Email
Website

```html
<!DOCTYPE html>
<html lang="en">
<head>
<meta charset="utf-8">
<title>Harbor Saver Club – Business Card</title>
<link href="https://fonts.googleapis.com/css2?family=Montserrat:wght@400;500;700&display=swap" rel="stylesheet">
<style>
  :root {
    --page-bg: #e9eaec;
    --card-bg: #ffffff;
    --royal: #3a5bbd;
    --sky: #46d8f2;
    --mint: #9df58a;
    --ink: #2a2a2e;
  }
  * { box-sizing: border-box; margin: 0; padding: 0; }
  html, body {
    width: 1200px; height: 1200px; overflow: hidden;
    background: var(--page-bg);
    font-family: "Montserrat", sans-serif;
  }
  .sheet {
    width: 1200px; height: 1200px;
    display: flex; flex-direction: column; align-items: center; justify-content: center;
    gap: 70px;
  }
  .card {
    position: relative;
    width: 900px; height: 510px;
    background: linear-gradient(180deg, #ffffff 0%, #f6f6f7 100%);
    border-radius: 44px;
    overflow: hidden;
    box-shadow: 0 14px 30px rgba(0,0,0,0.18);
  }
  .card__band {
    position: absolute; left: 0; right: 0; bottom: 0; height: 18px;
    display: flex;
  }
  .card__band span:nth-child(1) { flex: 0 0 44%; background: var(--royal); }
  .card__band span:nth-child(2) { flex: 0 0 27%; background: var(--sky); }
  .card__band span:nth-child(3) { flex: 1; background: var(--mint); }

  .brand {
    display: flex; align-items: center; gap: 16px;
    color: var(--royal); font-weight: 700; letter-spacing: 0.02em;
    text-transform: uppercase; line-height: 1;
  }
  .brand__dot { border-radius: 50%; background: var(--royal); flex: none; }

  /* front */
  .card--front .brand {
    position: absolute; right: 70px; top: 140px;
    font-size: 40px;
  }
  .card--front .brand__dot { width: 22px; height: 22px; }
  .contact {
    position: absolute; left: 80px; top: 210px;
  }
  .contact__id {
    border-left: 7px solid var(--royal);
    padding-left: 16px; margin-bottom: 26px;
  }
  .contact__name { font-size: 48px; font-weight: 700; color: var(--royal); line-height: 1; }
  .contact__role { font-size: 22px; font-weight: 500; color: var(--ink); margin-top: 6px; letter-spacing: 0.04em; }
  .contact__list { list-style: none; padding-left: 24px; }
  .contact__item {
    display: flex; align-items: center; gap: 14px;
    font-size: 25px; color: var(--ink); margin-bottom: 12px;
  }
  .contact__icon { width: 26px; height: 26px; flex: none; }

  /* back */
  .card--back .brand {
    position: absolute; left: 50%; top: 46%;
    transform: translate(-50%, -50%);
    font-size: 54px; white-space: nowrap;
  }
  .card--back .brand__dot { width: 30px; height: 30px; }
</style>
</head>
<body>
<main class="sheet">
  <section class="card card--front" aria-label="Business card front">
    <div class="contact">
      <div class="contact__id">
        <div class="contact__name">JOHN DOE</div>
        <div class="contact__role">POSITION</div>
      </div>
      <ul class="contact__list">
        <li class="contact__item">
          <svg class="contact__icon" viewBox="0 0 24 24" aria-hidden="true"><path fill="#3a5bbd" d="M6.6 10.8a15.1 15.1 0 0 0 6.6 6.6l2.2-2.2a1 1 0 0 1 1-.25 11.4 11.4 0 0 0 3.6.57 1 1 0 0 1 1 1V20a1 1 0 0 1-1 1A17 17 0 0 1 3 4a1 1 0 0 1 1-1h3.5a1 1 0 0 1 1 1c0 1.25.2 2.45.57 3.57a1 1 0 0 1-.25 1z"/></svg>
          (000) 000 0000
        </li>
        <li class="contact__item">
          <svg class="contact__icon" viewBox="0 0 24 24" aria-hidden="true"><rect x="2" y="5" width="20" height="14" rx="1.5" fill="#3a5bbd"/><path d="M3 6l9 7 9-7" fill="none" stroke="#fff" stroke-width="1.6"/></svg>
          email@youremail.com
        </li>
        <li class="contact__item">
          <svg class="contact__icon" viewBox="0 0 24 24" aria-hidden="true"><circle cx="12" cy="12" r="10" fill="#3a5bbd"/><g fill="none" stroke="#fff" stroke-width="1.2"><ellipse cx="12" cy="12" rx="4.5" ry="10"/><path d="M2 12h20M4 7h16M4 17h16M12 2v20"/></g></svg>
          www.yourwebsite.com
        </li>
      </ul>
    </div>
    <div class="brand"><span class="brand__dot"></span>Harbor Saver Club</div>
    <div class="card__band"><span></span><span></span><span></span></div>
  </section>

  <section class="card card--back" aria-label="Business card back">
    <div class="brand"><span class="brand__dot"></span>Harbor Saver Club</div>
    <div class="card__band"><span></span><span></span><span></span></div>
  </section>
</main>
</body>
</html>
```